Storm Restoration Contractor needs a professional business card design

Looking for a professional business card design. Not looking for your cheapo MS Word standard ones that are readily available. Dont want it to be cookie cutter look like ones readily available online. We just recently changed our logo and want to freshen up all our documents. Our company handles restoring a property back to a pre-loss condition after a storm damages it. For example, wind, hail, flood, fire losses.

Target Market(s)

Property Owners, Homeowners, Property Owners, Commercial Property Owners, Property Management Companies, Hail and Wind Damaged Properties

Industry/Entity Type

Construction Company

Contact Information for Business Card

Halden Facades
847-519-4073
847-519-6294 fax
www.haldenfacades.example
info@haldenfacades.example

Requirements
Must have
• Clean, Professional, fresh look
• Storm Restoration, Roofing, Siding, Windows
Nice to have
• If there is a way to incorporate storms that may be cool.

```html
<!DOCTYPE html>
<html lang="en">
<head>
<meta charset="utf-8">
<title>Halden Facades – Business Card</title>
<link href="https://fonts.googleapis.com/css2?family=Arimo:wght@400;700&display=swap" rel="stylesheet">
<style>
  :root {
    --page-bg: #e6e3df;
    --card-bg: #141516;
    --card-sheen: #1e2021;
    --brand-blue: #2b8fd6;
    --text-light: #f2f2f2;
    --text-muted: #d8d8d8;
    --divider: #2f6fa8;
  }
  * { box-sizing: border-box; margin: 0; padding: 0; }
  html, body {
    width: 1200px; height: 1200px; overflow: hidden;
    background: var(--page-bg);
    font-family: "Arimo", Arial, sans-serif;
  }
  .sheet {
    width: 1200px; height: 1200px;
    display: flex; flex-direction: column; align-items: center; justify-content: center;
    gap: 80px;
  }
  .card {
    position: relative;
    width: 840px; height: 480px;
    background: linear-gradient(135deg, var(--card-sheen) 0%, var(--card-bg) 55%, var(--card-bg) 100%);
    border-radius: 4px;
    box-shadow: 0 14px 30px rgba(0,0,0,.25);
    overflow: hidden;
  }
  .brand {
    display: flex; align-items: center; gap: 22px;
  }
  .brand-mark {
    width: 72px; height: 72px; border-radius: 50%;
    border: 7px solid var(--brand-blue);
    flex-shrink: 0;
  }
  .brand-name {
    color: var(--brand-blue);
    font-weight: 700;
    font-size: 34px;
    letter-spacing: 4px;
    text-transform: uppercase;
    white-space: nowrap;
  }

  /* Contact side */
  .card--contact .brand {
    position: absolute; left: 50px; top: 50%; transform: translateY(-50%);
  }
  .card--contact .brand-mark { width: 60px; height: 60px; border-width: 6px; }
  .card--contact .brand-name { font-size: 26px; letter-spacing: 3px; }
  .divider {
    position: absolute; left: 440px; top: 90px;
    width: 1px; height: 300px;
    background: linear-gradient(to bottom, transparent, var(--divider), transparent);
  }
  .contact {
    position: absolute; right: 56px; top: 70px; bottom: 70px;
    display: flex; flex-direction: column; justify-content: space-between;
    text-align: right;
  }
  .person-name { color: var(--text-light); font-size: 36px; font-weight: 400; }
  .person-role { color: var(--brand-blue); font-size: 22px; margin-top: 2px; }
  .contact-list { list-style: none; display: flex; flex-direction: column; gap: 8px; }
  .contact-item {
    display: flex; justify-content: flex-end; align-items: center; gap: 12px;
    color: var(--text-muted); font-size: 20px;
  }
  .contact-icon {
    width: 22px; height: 22px; border-radius: 3px;
    background: var(--brand-blue);
    display: flex; align-items: center; justify-content: center;
  }
  .contact-icon svg { width: 14px; height: 14px; fill: none; stroke: #fff; stroke-width: 2; }

  /* Logo side */
  .card--logo { display: flex; align-items: center; justify-content: center; }
</style>
</head>
<body>
<main class="sheet">
  <section class="card card--contact">
    <div class="brand">
      <span class="brand-mark"></span>
      <span class="brand-name">Halden Facades</span>
    </div>
    <span class="divider"></span>
    <div class="contact">
      <div class="person">
        <p class="person-name">Marcus Dale</p>
        <p class="person-role">Owner</p>
      </div>
      <ul class="contact-list">
        <li class="contact-item">847-519-4073
          <span class="contact-icon"><svg viewBox="0 0 16 16"><path d="M4 2l2 3-1.5 1.5a8 8 0 0 0 5 5L11 10l3 2-1 2.5A11 11 0 0 1 1.5 3z"/></svg></span>
        </li>
        <li class="contact-item">847-519-6294
          <span class="contact-icon"><svg viewBox="0 0 16 16"><rect x="3" y="2" width="10" height="12"/><path d="M5 6h6M5 9h6"/></svg></span>
        </li>
        <li class="contact-item">info@haldenfacades.example
          <span class="contact-icon"><svg viewBox="0 0 16 16"><rect x="2" y="4" width="12" height="8"/><path d="M2 4l6 5 6-5"/></svg></span>
        </li>
        <li class="contact-item">www.haldenfacades.example
          <span class="contact-icon"><svg viewBox="0 0 16 16"><circle cx="8" cy="8" r="6"/><path d="M2 8h12M8 2c3 3 3 9 0 12M8 2c-3 3-3 9 0 12"/></svg></span>
        </li>
      </ul>
    </div>
  </section>

  <section class="card card--logo">
    <div class="brand">
      <span class="brand-mark"></span>
      <span class="brand-name">Halden Facades</span>
    </div>
  </section>
</main>
</body>
</html>
```